Business card for Autism Consultancy

I need a double-sided business card for Brightpath Kinder Consultancy
Please try to use the colours and graphics in line with our website www.brightpathkinder.nz
Front side
Logo and the name of the company – Brightpath Kinder Consultancy
We use Child-Centred, Modern and Innovative approaches
Teaching autistic children to bond, laugh and play
www.brightpathkinder.nz
info@brightpathkinder.nz
phone +64 09 37 815 66
Back side
Photo
Orla Fennimore
Founder
Postgraduate Autism (Children) Specialist (with Merit)
Qualified by the Faculty of Learning Support and Wellbeing Studies (FLSW), University of Thornvale
orla@brightpathkinder.nz
phone +64 937 815 66
mobile: +64 20 6283 9145
Please do not convert the text fields to outlines, i.e. I need to be able to edit any text after.
The final design should be either in Adobe Illustrator or Adobe Photoshop format.
The Specs for the business card are:
Full Bleed Size
94 x 58 mm
1110 x 685 pixels
Document Trim Size
91 x 55 mm
1075 x 650 pixels

```html
<!DOCTYPE html>
<html lang="en">
<head>
<meta charset="utf-8">
<title>Brightpath Kinder Consultancy – Business Card</title>
<link href="https://fonts.googleapis.com/css2?family=Roboto:wght@400;500;700&display=swap" rel="stylesheet">
<style>
  :root{
    --navy:#172a5c;
    --teal:#3cc4bd;
    --yellow:#f7c91c;
    --grey:#9a9a9a;
    --white:#ffffff;
    --stage:#e6e7ea;
  }
  *{box-sizing:border-box;margin:0;padding:0}
  html,body{width:1200px;height:1200px;overflow:hidden}
  body{background:var(--stage);font-family:"Roboto",sans-serif;color:var(--navy);position:relative}
  .card{position:absolute;left:160px;width:880px;height:532px;background:var(--white);border-radius:34px;overflow:hidden;box-shadow:0 6px 18px rgba(0,0,0,.12)}
  .card--front{top:44px}
  .card--back{top:624px}

  .brand{position:absolute;display:flex;align-items:center}
  .brand__dot{border-radius:50%;background:var(--yellow);flex:none}
  .brand__words{display:flex;flex-direction:column;align-items:flex-end}
  .brand__name{font-weight:700;color:var(--navy);white-space:nowrap;line-height:1}
  .brand__sub{font-weight:500;color:var(--grey);letter-spacing:.08em;line-height:1}

  .card--front .brand{left:120px;top:90px}
  .card--front .brand__dot{width:110px;height:110px;margin-right:34px}
  .card--front .brand__name{font-size:52px}
  .card--front .brand__sub{font-size:36px;margin-top:14px}

  .tagline{position:absolute;left:0;right:0;top:292px;text-align:center;color:var(--grey);font-size:17px;font-weight:500;text-transform:uppercase;letter-spacing:.02em;line-height:1}
  .tagline__rule{display:block;width:300px;height:2px;background:var(--teal);margin:9px auto 9px}

  .front-band{position:absolute;left:0;right:0;top:400px;height:76px;background:var(--navy);display:flex;align-items:center;justify-content:center;gap:16px;color:var(--white);font-size:21px;font-weight:500}
  .front-band__item{display:flex;align-items:center;gap:7px}
  .front-band__sep{opacity:.9}
  .icon{width:20px;height:20px;flex:none}

  .portrait{position:absolute;left:84px;top:32px;width:250px;height:250px;border-radius:50%;border:2px solid var(--navy);padding:6px}
  .portrait__fill{width:100%;height:100%;border-radius:50%;background:radial-gradient(circle at 50% 40%,#e9c2a6 0%,#b98366 45%,#5a3b2a 100%)}
  .person{position:absolute;left:60px;top:300px}
  .person__name{font-size:34px;font-weight:700;line-height:1.1}
  .person__role{font-size:22px;color:var(--teal);margin-bottom:14px}
  .person__quals{font-size:16.5px;line-height:1.3}
  .person__quals p+p{margin-top:4px}

  .card--back .brand{right:90px;top:58px}
  .card--back .brand__dot{width:80px;height:80px;margin-right:22px}
  .card--back .brand__name{font-size:36px}
  .card--back .brand__sub{font-size:26px;margin-top:10px}

  .contacts{position:absolute;right:70px;top:350px;display:flex;flex-direction:column;align-items:flex-end;gap:8px;font-size:20px;font-weight:500}
  .contacts__item{display:flex;align-items:center;gap:10px}
  .contacts .icon{color:var(--teal)}

  .back-band{position:absolute;left:0;right:0;bottom:0;height:44px;background:var(--navy)}
</style>
</head>
<body>

<section class="card card--front">
  <div class="brand">
    <span class="brand__dot"></span>
    <div class="brand__words">
      <span class="brand__name">Brightpath Kinder</span>
      <span class="brand__sub">CONSULTANCY</span>
    </div>
  </div>

  <p class="tagline">We use child-centred, modern and innovative approaches
    <span class="tagline__rule"></span>Teaching autistic children to bond, laugh and play</p>

  <div class="front-band">
    <span class="front-band__item">
      <svg class="icon" viewBox="0 0 20 20" fill="none" stroke="var(--teal)" stroke-width="1.6"><circle cx="10" cy="10" r="8"/><ellipse cx="10" cy="10" rx="3.5" ry="8"/><line x1="2" y1="10" x2="18" y2="10"/></svg>
      www.brightpathkinder.nz</span>
    <span class="front-band__sep">|</span>
    <span class="front-band__item">
      <svg class="icon" viewBox="0 0 20 20" fill="none" stroke="var(--teal)" stroke-width="1.6"><rect x="2" y="5" width="16" height="11" rx="1"/><polyline points="2,5 10,11 18,5"/></svg>
      info@brightpathkinder.nz</span>
    <span class="front-band__sep">|</span>
    <span class="front-band__item">
      <svg class="icon" viewBox="0 0 20 20" fill="var(--teal)"><path d="M5 2l3 3-2 2.5c1 2.3 2.8 4.1 5 5L13.5 10l3 3-2 3C9 16 4 11 3 4.5z"/></svg>
      +64 09 37 815 66</span>
  </div>
</section>

<section class="card card--back">
  <div class="portrait"><div class="portrait__fill" role="img" aria-label="Portrait photo of Orla Fennimore"></div></div>

  <div class="person">
    <h1 class="person__name">Orla Fennimore</h1>
    <p class="person__role">Founder</p>
    <div class="person__quals">
      <p>Postgraduate Autism (Children)<br>Specialist (with Merit)</p>
      <p>Qualified by the Faculty of Learning Support<br>and Wellbeing Studies (FLSW), University of Thornvale</p>
    </div>
  </div>

  <div class="brand">
    <span class="brand__dot"></span>
    <div class="brand__words">
      <span class="brand__name">Brightpath Kinder</span>
      <span class="brand__sub">CONSULTANCY</span>
    </div>
  </div>

  <div class="contacts">
    <span class="contacts__item">orla@brightpathkinder.nz
      <svg class="icon" viewBox="0 0 20 20" fill="none" stroke="currentColor" stroke-width="1.6"><rect x="2" y="5" width="16" height="11" rx="1"/><polyline points="2,5 10,11 18,5"/></svg></span>
    <span class="contacts__item">+64 937 815 66
      <svg class="icon" viewBox="0 0 20 20" fill="currentColor"><path d="M5 2l3 3-2 2.5c1 2.3 2.8 4.1 5 5L13.5 10l3 3-2 3C9 16 4 11 3 4.5z"/></svg></span>
    <span class="contacts__item">+64 20 6283 9145
      <svg class="icon" viewBox="0 0 20 20" fill="none" stroke="currentColor" stroke-width="1.6"><rect x="6" y="2" width="8" height="16" rx="1.5"/><line x1="9" y1="15" x2="11" y2="15"/></svg></span>
  </div>

  <div class="back-band"></div>
</section>

</body>
</html>
```